Business card for builder specialising in renovations.

Need a card for our building business. Business name is under Martin Pelloe.
Have licence number on card ( 527916K)
Contact number (0400 382 615)
Want to work on logo for some business cards and shirts - something with MP or MPB or open to ideas??
No animations, No hammers. Something sharp and eye catching.
Highlight that we are a renovation specialist. Simple on front with extra details on back with some lines to jot down things.

Target Market(s)

Renovators

Industry/Entity Type

Building

Contact Information for Business Card

2 sided with room on back to jot things down.
Extra details on back so front can be simple ..like, renovations, bathrooms, decks, extensions, new builds,

Logo Text

MP

Font styles to use
Serif

Requirements
Must have
• Eye catching design .
• Name : Martin pelloe
• Licence number
• Contact number - 0400382615
Nice to have
• Some logo design that we can carry through to other forms of advertising
• Local builder
• Quality work
Should not have
• No animations

```html
<!DOCTYPE html>
<html lang="en">
<head>
<meta charset="utf-8">
<title>Martin Pelloe – Business Card</title>
<link rel="stylesheet" href="https://fonts.googleapis.com/css2?family=Source+Sans+3:wght@700&family=Questrial&display=swap">
<style>
  :root {
    --page: #ebe8e4;
    --card: #959392;
    --ink: #ffffff;
    --ink-soft: rgba(255, 255, 255, 0.7);
    --accent: #e5141b;
    --shadow: rgba(0, 0, 0, 0.18);
  }
  * { margin: 0; padding: 0; box-sizing: border-box; }
  html, body {
    width: 1200px;
    height: 1200px;
    overflow: hidden;
    background: var(--page);
  }
  .canvas {
    position: relative;
    width: 1200px;
    height: 1200px;
  }
  .card {
    position: absolute;
    left: 254px;
    width: 707px;
    height: 403px;
    background: var(--card);
    box-shadow: 0 4px 12px var(--shadow);
    overflow: hidden;
  }
  .card--front { top: 181px; }
  .card--back  { top: 616px; }

  .brand-square {
    position: absolute;
    background: var(--accent);
  }
  .card--front .brand-square { left: 320px; top: 95px; width: 68px; height: 68px; }
  .card--back  .brand-square { left: 126px; top: 60px; width: 68px; height: 68px; }

  .wordmark {
    position: absolute;
    font-family: "Source Sans 3", sans-serif;
    font-weight: 700;
    color: var(--ink);
    white-space: nowrap;
    letter-spacing: -2px;
    line-height: 1;
  }
  .card--front .wordmark {
    left: 0; right: 0;
    top: 226px;
    text-align: center;
    font-size: 72px;
  }
  .card--back .wordmark {
    right: 91px;
    top: 152px;
    font-size: 52px;
  }

  .tagline {
    position: absolute;
    left: 0; right: 0;
    top: 318px;
    text-align: center;
    font-family: "Questrial", sans-serif;
    font-size: 20px;
    letter-spacing: 4px;
    text-transform: uppercase;
    color: var(--ink);
  }

  .services {
    position: absolute;
    right: 46px;
    top: 40px;
    width: 360px;
    text-align: right;
    font-family: "Questrial", sans-serif;
    font-size: 16px;
    line-height: 26px;
    color: var(--ink);
  }

  .divider {
    position: absolute;
    left: 30px;
    top: 220px;
    width: 677px;
    height: 10px;
  }

  .details {
    position: absolute;
    right: 45px;
    top: 270px;
    font-family: "Questrial", sans-serif;
    font-size: 27px;
    color: var(--ink);
    text-align: center;
    line-height: 50px;
    white-space: nowrap;
  }

  .notes {
    position: absolute;
    left: 40px;
    top: 246px;
    width: 200px;
  }
  .notes__label {
    font-family: "Questrial", sans-serif;
    font-size: 14px;
    letter-spacing: 2px;
    text-transform: uppercase;
    color: var(--ink);
    margin-bottom: 6px;
  }
  .notes__line {
    height: 34px;
    border-bottom: 1px solid var(--ink-soft);
  }
</style>
</head>
<body>
<main class="canvas">
  <section class="card card--front" aria-label="Card front">
    <div class="brand-square" aria-hidden="true"></div>
    <h1 class="wordmark">Martin Pelloe</h1>
    <p class="tagline">Renovation Specialist</p>
  </section>

  <section class="card card--back" aria-label="Card back">
    <div class="brand-square" aria-hidden="true"></div>
    <p class="services">Renovations · Bathrooms · Decks<br>Extensions · New Builds</p>
    <h2 class="wordmark">Martin Pelloe</h2>
    <svg class="divider" viewBox="0 0 677 10" preserveAspectRatio="none" aria-hidden="true">
      <polygon points="0,2 677,3 677,9" fill="#ffffff"/>
    </svg>
    <div class="notes">
      <p class="notes__label">Notes</p>
      <div class="notes__line"></div>
      <div class="notes__line"></div>
      <div class="notes__line"></div>
    </div>
    <div class="details">
      <p class="details__phone">Contact Number: 0400382615</p>
      <p class="details__licence">License Number: 527916K</p>
    </div>
  </section>
</main>
</body>
</html>
```